Pull Up Banner - Recruitment Company

We would like a design for a pull up banner.

For context: we are a recruitment business. We specialise in helping people in healthcare industry to find jobs in Australia.

I have come up with several ideas and text for the banner. Feel free to use the following as you see appropriate:

- Our logo (see attached)
- 'Healthcare Recruitment Agency'
- Some sort of imagine / cartoon of medical professionals (ie. doctor, nurse, physiotherapist, speech pathologist). A cartoon is more friendly than committing to a photo
- 'Empowering your next career move'
- 'Discover tailored opportunities based on your career preferences'
- Dot points (allied health, nursing, medical imaging)
- Contact info at the bottom including our website (www.pellatalent.com.au, our Instagram handle @pellatalent, Mobile: XXXX XXX XXX. The title section for contact information could be 'Get in touch:'

Feel free to submit a couple of designs and we can merge aspects that look good on your designs and find the perfect fit.
Thank you
Updates

Hello,

Thank you for your initial submissions to this project. I appreciate the time you've invested.

After reviewing the first attempt, I'd like to share some feedback and initial observations:

- Professionalism and engagement: Is the overall appearance of the banner professional? It's crucial that we have a high-quality design as this will represent our business.

- Image selection: The image (whether cartoon or real people) appears quite generic. Please consider submitting the banner with a few different photos in the middle for us to choose from. Ensure the image is a good fit and not simply a generic stock photo.

- Contact section: Kindly remove the phone number; we no longer wish to include it on the banner. Instead, please include our website (www.pellatalent.com.au) and Instagram handle (@pellatalent).

- Color scheme: White, black, and red/pink are preferred, or alternatively, blue. However, please avoid incorporating too many different colors as it may detract from the professional appearance.

We will be printing the design on a banner and require it to look professional and engaging.

Thank you once again for your submissions. I hope the feedback provided above is helpful.

Warm regards,

Target Market(s)

Allied Health Australia

Font styles to use
Serif

Colors
0054AA
0677BA
7BADD7
CADEEF
E8F1F8
0094D4
00A9DD
6FCCEA
C7EBF8
E9F6FB
EB3D1F
EC4F4E
F09395
F8D3D4
FCEDEE

```html
<!DOCTYPE html>
<html lang="en">
<head>
<meta charset="utf-8">
<title>Pella Talent – Healthcare Recruitment Agency Pull Up Banner</title>
<link href="https://fonts.googleapis.com/css2?family=League+Spartan:wght@300;400;700;800&family=Poppins:wght@500;600;700&display=swap" rel="stylesheet">
<style>
  :root {
    --page: #eceef3;
    --navy: #0a1685;
    --navy-deep: #0b1058;
    --royal: #3545d8;
    --sky: #7ba4ee;
    --ink: #2a2a2a;
    --white: #ffffff;
    --rule: #d9d9de;
    --lilac: #d08ad8;
    --lilac-soft: #f1d5f2;
  }
  * { margin: 0; padding: 0; box-sizing: border-box; }
  html, body { width: 1200px; height: 2400px; overflow: hidden; background: var(--page); }
  .banner {
    position: absolute; left: 83px; top: 0;
    width: 1033px; height: 2400px;
    background: var(--navy);
    overflow: hidden;
  }
  .backdrop { position: absolute; inset: 0; width: 100%; height: 100%; }
  .brand-name {
    position: absolute; top: 120px; left: 0; width: 100%;
    text-align: center;
    font-family: "League Spartan", sans-serif;
    font-weight: 800; font-size: 104px; letter-spacing: 6px;
    color: var(--white); line-height: 1;
  }
  .headline {
    position: absolute; top: 330px; left: 0; width: 100%;
    text-align: center;
    font-family: "League Spartan", sans-serif;
    font-weight: 800; line-height: 0.86; letter-spacing: -2px;
  }
  .headline .lead { display: block; font-size: 112px; color: var(--sky); }
  .headline .main { display: block; font-size: 134px; color: var(--white); }
  .scene-art {
    position: absolute; left: 89px; top: 690px;
    width: 887px; height: 824px;
    border-radius: 40px;
    background: linear-gradient(160deg, var(--lilac-soft) 0%, var(--lilac) 45%, var(--royal) 100%);
    opacity: 0.9;
  }
  .pitch {
    position: absolute; top: 1636px; left: 0; width: 100%;
    text-align: center; color: var(--ink);
    font-family: "League Spartan", sans-serif; line-height: 0.92;
  }
  .pitch .light { display: block; font-weight: 300; font-size: 88px; letter-spacing: -2px; }
  .pitch .bold { display: block; font-weight: 800; font-size: 88px; letter-spacing: -1px; }
  .tagline {
    position: absolute; top: 1800px; left: 0; width: 100%;
    text-align: center;
    font-family: "Poppins", sans-serif; font-weight: 600;
    font-size: 48px; letter-spacing: -1px; color: var(--ink);
  }
  .specialties {
    position: absolute; top: 1930px; left: 40px; right: 40px; height: 150px;
    display: flex;
  }
  .specialty {
    display: flex; flex-direction: column; align-items: center; justify-content: space-between;
    padding: 10px 0 0;
    font-family: "Poppins", sans-serif; font-weight: 500; font-size: 34px; color: var(--ink);
  }
  .specialty svg { width: 72px; height: 72px; }
  .specialty.allied { width: 332px; }
  .specialty.nursing { width: 229px; border-left: 2px solid var(--rule); border-right: 2px solid var(--rule); }
  .specialty.imaging { flex: 1; }
  .contact-title {
    position: absolute; top: 2118px; left: 0; width: 100%;
    text-align: center;
    font-family: "Poppins", sans-serif; font-weight: 700;
    font-size: 52px; letter-spacing: 6px; color: var(--royal);
  }
  .website {
    position: absolute; top: 2183px; left: 93px; width: 831px; height: 84px;
    border-radius: 42px; background: var(--navy);
    display: flex; align-items: center; justify-content: center;
    font-family: "Poppins", sans-serif; font-weight: 700;
    font-size: 44px; letter-spacing: 3px; color: var(--white);
  }
  .socials {
    position: absolute; top: 2292px; left: 0; width: 100%;
    display: flex; justify-content: center; gap: 16px;
  }
  .socials span { width: 46px; height: 46px; border-radius: 50%; background: var(--royal); }
</style>
</head>
<body>
  <main class="banner">
    <svg class="backdrop" viewBox="186 226 914 2124" preserveAspectRatio="none" aria-hidden="true">
      <polygon points="186,795 560,1010 186,1190" fill="#0b1058"/>
      <polygon points="186,1190 1100,775 1100,1270 186,1680" fill="#3545d8"/>
      <polygon points="1100,1270 1100,1615 700,1460" fill="#0b1058"/>
      <polygon points="186,1680 700,1455 1100,1615 1100,2350 186,2350" fill="#ffffff"/>
    </svg>

    <div class="brand-name">PELLA TALENT</div>

    <h1 class="headline">
      <span class="lead">HEALTHCARE</span>
      <span class="main">RECRUITMENT</span>
      <span class="main">AGENCY</span>
    </h1>

    <div class="scene-art" role="img" aria-label="Isometric illustration of a physiotherapy room: a clinician treating a patient's knee on a treatment table, with a wheelchair, exercise ball, plant, cabinet and an X-ray on the wall"></div>

    <h2 class="pitch">
      <span class="light">EMPOWER YOUR</span>
      <span class="bold">NEXT CAREER MOVE</span>
    </h2>
    <p class="tagline">Tailored opportunities that fit you</p>

    <ul class="specialties">
      <li class="specialty allied">
        <svg viewBox="0 0 72 72" aria-hidden="true">
          <path d="M36 50 L18 33 A10 10 0 0 1 36 20 A10 10 0 0 1 54 33 Z" fill="#0a1685"/>
          <polyline points="8,32 24,32 30,24 36,40 42,30 64,30" fill="none" stroke="#ffffff" stroke-width="3"/>
          <path d="M10 58 Q30 66 62 52" fill="none" stroke="#3545d8" stroke-width="6" stroke-linecap="round"/>
        </svg>
        Allied Health
      </li>
      <li class="specialty nursing">
        <svg viewBox="0 0 72 72" aria-hidden="true">
          <rect x="14" y="14" width="44" height="44" rx="10" fill="#3545d8"/>
          <rect x="31" y="22" width="10" height="28" fill="#ffffff"/>
          <rect x="22" y="31" width="28" height="10" fill="#ffffff"/>
        </svg>
        Nursing
      </li>
      <li class="specialty imaging">
        <svg viewBox="0 0 72 72" aria-hidden="true">
          <path d="M40 14 A22 22 0 1 0 40 58" fill="none" stroke="#3545d8" stroke-width="9"/>
          <rect x="22" y="32" width="44" height="8" fill="#0a1685"/>
          <rect x="46" y="40" width="4" height="18" fill="#0a1685"/>
          <rect x="20" y="58" width="40" height="4" fill="#0a1685"/>
        </svg>
        Medical Imaging
      </li>
    </ul>

    <p class="contact-title">GET IN TOUCH</p>
    <p class="website">www.pellatalent.com.au</p>
    <div class="socials" aria-hidden="true"><span></span><span></span><span></span></div>
  </main>
</body>
</html>
```